Dufresne Roofing

Want a professional looking business card

Industry/Entity Type

Business

Contact Information for Business Card

Marc Dufresne ( Owner) marc@dufresneroofing-example.com, www.dufresneroofing-example.com, Adress: 4217 County road 42 Wendover,ON K0A3M1

```html
<!DOCTYPE html>
<html lang="en">
<head>
<meta charset="utf-8">
<title>Dufresne Roofing – Business Card</title>
<link rel="stylesheet" href="https://fonts.googleapis.com/css2?family=Roboto:wght@400;500;700&family=Roboto+Condensed:wght@400;500&display=swap">
<style>
  :root {
    --backdrop: #2b2b2d;
    --brand-blue: #1a4688;
    --stripe-grey: #77787b;
    --card-white: #f1f1f1;
    --card-grey: #75777b;
    --text-light: #ffffff;
  }
  * { margin: 0; padding: 0; box-sizing: border-box; }
  html, body { width: 1200px; height: 960px; overflow: hidden; }
  body {
    background: var(--backdrop);
    font-family: "Roboto", Arial, sans-serif;
    position: relative;
  }
  .card {
    position: absolute;
    left: 320px;
    width: 600px;
    height: 343px;
    border-radius: 18px;
    overflow: hidden;
  }

  /* Back side */
  .card-back {
    top: 105px;
    background: var(--card-grey);
    display: flex;
    flex-direction: column;
    align-items: center;
    justify-content: center;
  }
  .card-back .brand-name {
    font-weight: 700;
    font-size: 36px;
    letter-spacing: 1px;
    color: var(--brand-blue);
    line-height: 1;
    text-align: center;
  }
  .card-back .brand-name .line-two {
    display: block;
    font-size: 19px;
    letter-spacing: 12px;
    margin-top: 8px;
    margin-right: -12px;
  }
  .card-back .brand-web {
    margin-top: 14px;
    font-size: 15px;
    letter-spacing: 2.5px;
    color: var(--text-light);
  }

  /* Front side */
  .card-front {
    top: 493px;
    background: var(--card-white);
  }
  .card-front .wave {
    position: absolute;
    inset: 0;
    width: 600px;
    height: 343px;
  }
  .card-front .brand-name {
    position: absolute;
    left: 42px;
    top: 58px;
    font-weight: 700;
    font-size: 32px;
    letter-spacing: 1px;
    color: var(--brand-blue);
    line-height: 1;
    text-align: center;
  }
  .card-front .brand-name .line-two {
    display: block;
    font-size: 18px;
    letter-spacing: 11px;
    margin-top: 8px;
    margin-right: -11px;
  }
  .holder {
    position: absolute;
    left: 78px;
    top: 274px;
    color: var(--text-light);
  }
  .holder-name {
    font-family: "Roboto Condensed", Arial, sans-serif;
    font-weight: 500;
    font-size: 23px;
    line-height: 1.1;
  }
  .holder-role {
    font-size: 14px;
    margin-top: 4px;
  }
  .contact {
    position: absolute;
    right: 30px;
    top: 214px;
    color: var(--text-light);
    font-size: 14px;
    text-align: right;
    line-height: 19px;
  }
  .address { margin-right: 20px; margin-bottom: 9px; }
  .contact-row {
    display: flex;
    justify-content: flex-end;
    align-items: center;
    gap: 6px;
  }
  .contact-row svg { width: 13px; height: 13px; flex: none; }
</style>
</head>
<body>

  <section class="card card-back" aria-label="Business card back">
    <div class="brand-name">DUFRESNE<span class="line-two">ROOFING</span></div>
    <div class="brand-web">www.dufresneroofing-example.com</div>
  </section>

  <section class="card card-front" aria-label="Business card front">
    <svg class="wave" viewBox="0 0 600 343" aria-hidden="true">
      <path d="M0 343 L0 328 C40 250 110 232 270 206 C440 180 545 158 600 0 L600 343 Z" fill="var(--brand-blue)"/>
      <path d="M0 316 C40 236 110 220 270 194 C440 168 540 146 592 0" fill="none" stroke="var(--stripe-grey)" stroke-width="7"/>
      <path d="M6 296 C50 228 120 212 270 186 C430 160 530 138 582 0" fill="none" stroke="var(--brand-blue)" stroke-width="3"/>
    </svg>

    <div class="brand-name">DUFRESNE<span class="line-two">ROOFING</span></div>

    <div class="holder">
      <div class="holder-name">MARC DUFRESNE</div>
      <div class="holder-role">OWNER</div>
    </div>

    <div class="contact">
      <div class="address">4217 County road 42<br>Wendover, ON K0A3M1</div>
      <div class="contact-row">613 555 0147
        <svg viewBox="0 0 24 24"><path fill="#fff" d="M6.6 10.8a15.1 15.1 0 0 0 6.6 6.6l2.2-2.2c.3-.3.7-.4 1-.2 1.1.4 2.3.6 3.6.6.6 0 1 .4 1 1V20c0 .6-.4 1-1 1A17 17 0 0 1 3 4c0-.6.4-1 1-1h3.5c.6 0 1 .4 1 1 0 1.3.2 2.5.6 3.6.1.3 0 .7-.2 1z"/></svg>
      </div>
      <div class="contact-row">marc@dufresneroofing-example.com
        <svg viewBox="0 0 24 24"><path fill="#fff" d="M2 5h20v14H2z"/><path fill="none" stroke="var(--brand-blue)" stroke-width="2" d="M2 6l10 7 10-7"/></svg>
      </div>
      <div class="contact-row">www.dufresneroofing-example.com
        <svg viewBox="0 0 24 24"><circle cx="12" cy="12" r="10" fill="#fff"/><path fill="none" stroke="var(--brand-blue)" stroke-width="1.6" d="M2 12h20M12 2c3 3 3 17 0 20M12 2c-3 3-3 17 0 20"/></svg>
      </div>
    </div>
  </section>

</body>
</html>
```